Business Card Design

We would like a business card that utilizes our current logo and keeps with the same feel - elegant and organic. Our farm isn't about mass production, it's about excellence, education, beautiful events and flowers - people, culture, and community.

Target Market(s)

Patrons to our farm who are interested in weddings, events, or our flowers and vegetables.

Contact Information for Business Card

Name, address, cell email (Danielle Hoskins, 2716 Wrenfield Rd, Millbrook, CO 80547, cell 30.412.6638, email danielle@wrenfieldacres.com)

```html
<!DOCTYPE html>
<html lang="en">
<head>
<meta charset="utf-8">
<title>Wrenfield Acres – Business Card</title>
<link rel="stylesheet" href="https://fonts.googleapis.com/css2?family=Tinos:ital@0;1&display=swap">
<style>
  :root {
    --backdrop: #e6e4e1;
    --card-white: #ffffff;
    --sage: #6d7f6f;
    --sage-faint: #dfe3de;
    --copper: #a8743c;
    --ink: #5a5f5a;
    --photo-light: #ece6e6;
    --photo-mid: #c9c3bb;
    --photo-green: #6f7d63;
    --photo-blush: #e8c6cb;
    --logo-on-photo: #ffffff;
  }
  html, body {
    margin: 0;
    padding: 0;
    width: 1200px;
    height: 900px;
    overflow: hidden;
    background: var(--backdrop);
    font-family: "Tinos", "Times New Roman", serif;
  }
  .canvas {
    position: relative;
    width: 1200px;
    height: 900px;
  }
  .card {
    position: absolute;
    left: 250px;
    width: 700px;
    height: 400px;
    border-radius: 26px;
    overflow: hidden;
    box-shadow: 0 6px 18px rgba(0,0,0,0.12);
  }
  .card--front { top: 30px; background: var(--card-white); }
  .card--back  { top: 470px; }

  .brand-name {
    position: absolute;
    margin: 0;
    font-weight: 400;
    line-height: 1;
    white-space: nowrap;
  }
  .card--front .brand-name {
    left: 60px;
    top: 95px;
    font-size: 44px;
    color: var(--sage);
  }
  .address {
    position: absolute;
    left: 440px;
    top: 38px;
    margin: 0;
    font-style: normal;
    font-size: 17px;
    line-height: 1.2;
    color: var(--ink);
  }
  .leaf-motif {
    position: absolute;
    left: 410px;
    top: 140px;
    width: 270px;
    height: 190px;
    border-radius: 50% 40% 50% 40%;
    background: radial-gradient(ellipse at center, var(--sage-faint) 0%, rgba(223,227,222,0) 70%);
  }
  .person {
    position: absolute;
    left: 90px;
    top: 210px;
  }
  .person-name {
    margin: 0;
    font-size: 29px;
    font-weight: 400;
    color: var(--sage);
    line-height: 1.1;
  }
  .person-role {
    margin: 2px 0 0;
    font-size: 18px;
    font-style: italic;
    color: var(--copper);
  }
  .contact {
    position: absolute;
    left: 100px;
    top: 285px;
    margin: 0;
    padding: 0;
    list-style: none;
    font-size: 19px;
    line-height: 1.3;
    color: var(--ink);
  }
  .contact-label {
    display: inline-block;
    width: 26px;
    color: var(--copper);
  }
  .photo {
    position: absolute;
    inset: 0;
    background:
      radial-gradient(ellipse at 78% 45%, var(--photo-blush) 0%, rgba(232,198,203,0) 35%),
      radial-gradient(ellipse at 45% 35%, #f4f1ea 0%, rgba(244,241,234,0) 30%),
      radial-gradient(ellipse at 60% 20%, var(--photo-green) 0%, rgba(111,125,99,0) 45%),
      linear-gradient(160deg, var(--photo-light) 0%, var(--photo-mid) 60%, #9e9a94 100%);
  }
  .card--back .brand-name {
    left: 100px;
    top: 290px;
    font-size: 46px;
    color: var(--logo-on-photo);
  }
</style>
</head>
<body>
  <main class="canvas">
    <section class="card card--front" aria-label="Business card front">
      <p class="brand-name">Wrenfield Acres</p>
      <address class="address">2716 Wrenfield Rd<br>Millbrook, CO<br>&nbsp;80547</address>
      <div class="leaf-motif" role="img" aria-label="Faint sage leafy branch decoration"></div>
      <div class="person">
        <h1 class="person-name">Danielle Hoskins</h1>
        <p class="person-role">owner</p>
      </div>
      <ul class="contact">
        <li><span class="contact-label">C</span>30.412.6638</li>
        <li><span class="contact-label">E</span>danielle@wrenfieldacres.com</li>
        <li><span class="contact-label">W</span>www.wrenfieldacres.com</li>
      </ul>
    </section>

    <section class="card card--back" aria-label="Business card back">
      <div class="photo" role="img" aria-label="Photograph of white and pink peonies with red buds in a rustic bucket"></div>
      <p class="brand-name">Wrenfield Acres</p>
    </section>
  </main>
</body>
</html>
```